Website Design for Wheels for Heroes.org - Donated Cars to Disabled Vets

Need a Wordpress website. The coding now, esp. the CDONT coding is not supported by many hosting sites. Looking for a landing page to generate leads.

Logo Text

look at current one for ideas

Coding

Coded - Design and coding required

Number of Pages Required

1 page

Requirements
Must have
• look at current website at www.wheelsforheroes.org
Nice to have
• look at this site: http://givemotortoservicemen.org

```html
<!DOCTYPE html>
<html lang="en">
<head>
<meta charset="utf-8">
<title>Wheels for Heroes – Donate Your Car</title>
<link rel="stylesheet" href="https://fonts.googleapis.com/css2?family=Raleway:wght@600;700&family=Open+Sans:ital,wght@0,400;0,600;0,700;1,400&display=swap">
<style>
:root{
  --blue:#1f5fb8;
  --blue-dark:#0d3276;
  --navy:#0b2f6b;
  --red:#a5150f;
  --form-red:#9b0d0d;
  --nav:#252a2c;
  --text:#555;
  --heading:#333;
  --white:#fff;
  --light:#f2f2f2;
}
*{box-sizing:border-box;margin:0;padding:0}
html,body{width:1200px;height:2568px;overflow:hidden}
body{font-family:"Open Sans",Arial,sans-serif;color:var(--text);background:var(--white);position:relative}
.wrap{width:880px;margin:0 auto;position:relative}
h1,h2,h3{font-family:"Raleway",Arial,sans-serif}

/* header */
.topbar{height:79px;background:linear-gradient(#2d6cc4,#1a55aa)}
.topbar .wrap{height:79px;display:flex;align-items:center;justify-content:space-between}
.brand{display:flex;align-items:center;gap:10px;color:var(--white);font-weight:700;font-size:22px}
.brand-dot{width:26px;height:26px;border-radius:50%;background:var(--red)}
.tollfree{color:var(--white);text-align:left;width:157px}
.tollfree small{display:block;font-size:12px;font-weight:700;letter-spacing:.3px}
.tollfree strong{font-size:22px}
.mainnav{height:48px;background:var(--nav)}
.mainnav ul{list-style:none;display:flex;justify-content:space-between;height:48px;align-items:center}
.mainnav a{color:var(--white);text-decoration:none;font-size:13px;font-weight:700;text-transform:uppercase}

/* hero */
.hero{height:542px;position:relative}
.hero-photo{position:absolute;inset:0;background:linear-gradient(180deg,#cfe0ea 0%,#9fb58a 30%,#8a6f58 48%,#c9b39e 70%,#b59c88 100%)}
.hero-title{position:absolute;left:240px;top:44px;width:360px;text-align:center;color:var(--red);font-size:26px;line-height:31px;font-weight:700}
.donate-form{position:absolute;left:657px;top:46px;width:381px;height:450px;background:var(--form-red);padding:0 17px;color:var(--white)}
.donate-form .call{text-align:center;padding-top:10px;font-size:16px}
.donate-form .call strong{display:block;font-size:25px;font-weight:700;margin-top:2px}
.donate-form .sep{height:1px;background:rgba(255,255,255,.25);margin:12px -17px 0}
.donate-form .note{text-align:center;font-style:italic;font-size:12px;margin:10px 0 14px}
.row{display:flex;gap:7px;margin-bottom:9px}
.field{flex:1;height:34px;background:var(--white);font-size:11px;font-style:italic;color:#888;padding:10px 10px;position:relative}
.field.select::after{content:"";position:absolute;right:10px;top:15px;border:4px solid transparent;border-top-color:#555}
.submit{margin-top:13px;height:42px;background:var(--nav);display:flex;align-items:center;justify-content:center;font-size:13px;font-weight:700;letter-spacing:.2px}

/* program */
.program{height:415px;position:relative}
.bar{position:absolute;top:0;height:7px;background:var(--blue-dark)}
.bar.red{background:var(--red)}
.section-title{color:var(--blue-dark);font-size:26px;font-weight:700}
.program .section-title{padding-top:31px}
.features{display:flex;margin-top:68px;margin-left:-22px}
.feature{width:230px;text-align:center}
.feature svg{height:56px;display:block;margin:0 auto}
.feature h3{font-family:"Open Sans",sans-serif;color:var(--red);font-size:13px;font-weight:600;line-height:20px;margin-top:28px;min-height:40px}
.feature p{font-size:11px;line-height:19px;margin-top:12px;padding:0 20px}

/* tax */
.tax{height:484px;position:relative;border-top:2px solid #ddd;background:linear-gradient(90deg,#fafafa,#e9e9e9)}
.tax-photo{position:absolute;left:0;top:28px;width:540px;height:420px;background:radial-gradient(ellipse at 45% 55%,#d6d8da 0%,#a8abae 45%,#eceded 75%);border-radius:0 40% 10% 0}
.tax-text{position:absolute;left:567px;top:0;width:470px}
.tax .bar{left:0;width:291px;top:-2px}
.tax .section-title{padding-top:46px;line-height:38px}
.tax p{font-size:11px;line-height:19px;margin-top:12px}
.tax h3{color:var(--red);font-size:17px;margin-top:30px}

/* why */
.why{height:474px}
.why h2{text-align:center;color:var(--heading);font-size:28px;font-weight:600;padding-top:76px}
.reasons{display:grid;grid-template-columns:310px 310px 260px;row-gap:51px;margin-top:52px}
.reason{display:flex;gap:10px}
.reason .ic{width:77px;height:77px;flex:none;border-radius:50%;background:var(--navy);border:3px solid var(--white);box-shadow:0 0 0 2px var(--navy);display:flex;align-items:center;justify-content:center}
.reason h3{font-family:"Open Sans",sans-serif;color:var(--red);font-size:14px;font-weight:600;line-height:19px;margin-top:6px}
.reason p{font-size:11px;line-height:19px;margin-top:4px;width:175px}

/* cta */
.cta{height:432px;background:linear-gradient(135deg,#0f3a83,#0a2b68);position:relative;color:var(--white)}
.cta .bar{left:161px;width:293px}
.cta h2{position:absolute;left:161px;top:62px;font-size:28px;font-weight:700}
.cta p{position:absolute;left:161px;top:120px;width:430px;font-size:11px;line-height:20px}
.cta ul{position:absolute;left:161px;top:208px;list-style:none;font-size:14px}
.cta li{height:34px;display:flex;align-items:center;gap:18px}
.cta li::before{content:"›";width:13px;height:13px;border-radius:50%;background:var(--white);color:var(--navy);font-size:12px;line-height:11px;text-align:center;font-weight:700}
.cta-photo{position:absolute;left:633px;top:81px;width:475px;height:270px;background:radial-gradient(ellipse at 50% 55%,#e3251f 0%,#b5120f 55%,rgba(10,43,104,0) 72%)}

/* footer */
.stripes{height:12px;background:linear-gradient(var(--white) 0 2px,var(--red) 2px 6px,var(--white) 6px 8px,var(--blue-dark) 8px)}
.footer{height:82px}
.footer .wrap{display:flex;align-items:center;height:82px}
.badge{width:60px;height:60px;border-radius:50%;background:#dfe8f0;border:2px solid #6c93b8}
.badge.rect{width:85px;height:32px;border-radius:3px;background:#e6e6e6;border:none;margin-left:18px}
.vdiv{width:1px;height:42px;background:#ccc;margin:0 14px}
.social{display:flex;gap:6px}
.social span{width:31px;height:31px;border-radius:50%;background:#3b6db3}
.social span:nth-child(1){background:#45a9e0}
.social span:nth-child(3){background:#1f6fa8}
.social span:nth-child(4){background:#d2503c}
.legal{margin-left:auto;margin-right:22px;font-size:11px;color:#333;line-height:19px}
.legal a{color:#333;text-decoration:none;margin-right:10px}
.code{font-size:11px;color:#333}
</style>
</head>
<body>

<header class="topbar">
  <div class="wrap">
    <div class="brand"><span class="brand-dot"></span>Wheels for Heroes</div>
    <div class="tollfree"><small>CALL TOLL-FREE</small><strong>1-800-555-0142</strong></div>
  </div>
</header>
<nav class="mainnav">
  <ul class="wrap">
    <li><a href="#">Why Donate Your Car</a></li>
    <li><a href="#">About</a></li>
    <li><a href="#">Our Charity</a></li>
    <li><a href="#">Blog</a></li>
    <li><a href="#">Donate Your Car</a></li>
    <li><a href="#">FAQ</a></li>
    <li><a href="#">Contact</a></li>
  </ul>
</nav>

<section class="hero">
  <div class="hero-photo" role="img" aria-label="Soldier in uniform greeting a child on a brick path by a wooden fence"></div>
  <h1 class="hero-title">Donate Your Car: Full Tax Deduction - Running or Not</h1>
  <form class="donate-form">
    <div class="call">Call Today to Donate<strong>1-800-555-0142</strong></div>
    <div class="sep"></div>
    <div class="note">Or Fill out the form below to instantly donate online</div>
    <div class="row"><div class="field">Name</div><div class="field">Last Name</div></div>
    <div class="row"><div class="field">Phone:</div></div>
    <div class="row"><div class="field">Email:</div></div>
    <div class="row"><div class="field">Address</div><div class="field">City</div></div>
    <div class="row"><div class="field select">State</div><div class="field">Zip Code</div></div>
    <div class="row"><div class="field select">Choose year</div><div class="field">Model</div></div>
    <div class="submit">CLICK HERE TO DONATE NOW &#10148;</div>
  </form>
</section>

<section class="program">
  <div class="wrap">
    <div class="bar" style="left:0;width:293px"></div>
    <h2 class="section-title">Car Donation Program</h2>
    <div class="features">
      <div class="feature">
        <svg viewBox="0 0 90 56" width="90" role="img" aria-label="Map of the nation"><rect x="4" y="10" width="82" height="38" rx="10" fill="#0d3276"/></svg>
        <h3>Donations<br>Accepted Nationwide</h3>
        <p>Sed ut perspiciatis unde omnis sit voluptatem accusantium dolorue laudantiutem accusantmota.</p>
      </div>
      <div class="feature">
        <svg viewBox="0 0 64 56" width="64"><path d="M12 26 L18 10 H46 L52 26 H58 V46 H50 V52 H42 V46 H22 V52 H14 V46 H6 V26 Z" fill="#0d3276"/><path d="M20 14 H44 L48 26 H16 Z" fill="#fff"/><circle cx="16" cy="36" r="4" fill="#fff"/><circle cx="48" cy="36" r="4" fill="#fff"/></svg>
        <h3>All Vehicle<br>Types Welcome</h3>
        <p>Sed ut perspiciatis unde omnis sit voluptatem accusantium dolorue laudantiutem accusantmota.</p>
      </div>
      <div class="feature">
        <svg viewBox="0 0 46 56" width="46"><rect x="3" y="3" width="40" height="50" rx="3" fill="#0d3276"/><rect x="10" y="12" width="26" height="3" fill="#fff"/><rect x="10" y="20" width="26" height="3" fill="#fff"/><rect x="10" y="28" width="14" height="3" fill="#fff"/><rect x="10" y="36" width="14" height="3" fill="#fff"/><text x="31" y="45" font-size="16" font-weight="700" fill="#fff" text-anchor="middle" font-family="Open Sans,sans-serif">$</text></svg>
        <h3>Tax Deductible</h3>
        <p>Sed ut perspiciatis unde omnis sit voluptatem accusantium dolorue laudantiutem accusantmota.</p>
      </div>
      <div class="feature">
        <svg viewBox="0 0 76 56" width="76"><path d="M4 20 L20 6 L24 10 L10 24 Z" fill="#0d3276"/><path d="M6 24 V34" stroke="#0d3276" stroke-width="3"/><rect x="6" y="30" width="44" height="14" fill="#0d3276"/><path d="M50 18 H64 L72 30 V44 H50 Z" fill="#0d3276"/><path d="M54 22 H62 L67 30 H54 Z" fill="#fff"/><circle cx="18" cy="46" r="7" fill="#0d3276" stroke="#fff" stroke-width="2"/><circle cx="60" cy="46" r="7" fill="#0d3276" stroke="#fff" stroke-width="2"/></svg>
        <h3>Towing is Free</h3>
        <p>Sed ut perspiciatis unde omnis sit voluptatem accusantium dolorue laudantiutem accusantmota.</p>
      </div>
    </div>
  </div>
</section>

<section class="tax">
  <div class="tax-photo" role="img" aria-label="Silver sedan seen from the side"></div>
  <div class="tax-text">
    <div class="bar"></div>
    <h2 class="section-title">Tax Deduction Information<br>For Your Car Donation</h2>
    <p>Sed ut perspiciatis unde omnis iste natus error sit voluptatem accusantium doloremque ud antium, totam rem aperiam, eaque ipsa quae ab illo inventore veritatis et qua.</p>
    <h3>If Your Car Donation Sells for $500 Or Less</h3>
    <p>Sed ut perspiciatis unde omnis iste natus error sit voluptatem accusantium doloremque ud antium, totam rem aperiam, eaque ipsa quae ab illo inventore veritatis et quasi architectoea tae vitae dicta sunt explicabomo enim ipsam voluptatem quia voluptas sit aspernat</p>
    <h3>If Your Car Donation Sells for $501 Or More</h3>
    <p>Sed ut perspiciatis unde omnis iste natus error sit voluptatem accusantium doloremque ud antium, totam rem aperiam, eaque ipsa quae ab illo inventore veritatis et quasi architectoea tae vitae dicta sunt explicabomo enim ipsam voluptatem quia voluptas sit aspernat</p>
  </div>
</section>

<section class="why">
  <div class="wrap">
    <h2>Why Donate Your Car to Us?</h2>
    <div class="reasons">
      <div class="reason">
        <div class="ic"><svg width="30" height="30" viewBox="0 0 30 30"><path d="M3 3 H14 L27 16 L16 27 L3 14 Z" fill="#fff"/><circle cx="9" cy="9" r="2.5" fill="#0b2f6b"/></svg></div>
        <div><h3>Free Local Towing</h3><p>We will pick up your car donation, running or not, when it's most convenient, at home or work.</p></div>
      </div>
      <div class="reason">
        <div class="ic"><svg width="30" height="32" viewBox="0 0 30 32"><circle cx="12" cy="4" r="3.5" fill="#fff"/><path d="M11 9 V19 H21 L25 28" stroke="#fff" stroke-width="3.5" fill="none"/><path d="M8 14 A9 9 0 1 0 20 26" stroke="#fff" stroke-width="3" fill="none"/></svg></div>
        <div><h3>All Cars Accepted</h3><p>We take your car regardless of its condition or registration status.</p></div>
      </div>
      <div class="reason">
        <div class="ic"><svg width="24" height="30" viewBox="0 0 24 30"><path d="M2 2 H15 L22 9 V28 H2 Z" fill="#fff"/><path d="M15 2 V9 H22" fill="#0b2f6b"/></svg></div>
        <div><h3>Income Tax Deduction</h3><p>We issue you an IRS tax receipt &amp; offer the largest resale network to get you the highest tax</p></div>
      </div>
      <div class="reason">
        <div class="ic"><svg width="30" height="30" viewBox="0 0 30 30"><circle cx="15" cy="15" r="12" fill="#fff"/><path d="M9 8 Q14 10 12 15 Q9 18 11 23 M19 6 Q17 11 21 13 Q25 15 23 20" stroke="#0b2f6b" stroke-width="2.5" fill="none"/></svg></div>
        <div><h3>No Paperwork Hassles</h3><p>We take any car and handle everything; DMV, Smog and IRS paperwork.</p></div>
      </div>
      <div class="reason">
        <div class="ic"><span style="color:#fff;font-size:34px;font-weight:700;line-height:1">$</span></div>
        <div><h3>Car donations help<br>fund programs</h3><p>And benefit Heroes Support Fund.</p></div>
      </div>
      <div class="reason">
        <div class="ic"><svg width="30" height="30" viewBox="0 0 30 30"><circle cx="15" cy="15" r="12" fill="none" stroke="#fff" stroke-width="3"/><path d="M15 8 V15 H21" stroke="#fff" stroke-width="3" fill="none"/></svg></div>
        <div><h3>Schedule a Free Pickup</h3><p>Complete the form and a representative will call you to arrange a convenient time</p></div>
      </div>
    </div>
  </div>
</section>

<section class="cta">
  <div class="bar red"></div>
  <h2>Donate Your Car Today!</h2>
  <p>Sed ut perspiciatis unde omnis iste natus error sit voluptatem accusantium dolore mque laudantium, totam rem aperiam, eaque ipsa quae ab illo inventore veritatis et quasi architecto beatae vitae dicta sunt explicabomo dolorem ipsum quia.</p>
  <ul>
    <li>You have no costs.</li>
    <li>Free towing, running or not.</li>
    <li>We issue you an IRS tax receipt.</li>
    <li>We take care of all paperwork.</li>
    <li>And we take care of DMV &amp; Smog issues.</li>
  </ul>
  <div class="cta-photo" role="img" aria-label="Red hatchback car, front three-quarter view"></div>
</section>

<div class="stripes"></div>
<footer class="footer">
  <div class="wrap">
    <span class="badge" role="img" aria-label="Certification seal"></span>
    <span class="badge rect" role="img" aria-label="Security badge"></span>
    <span class="vdiv"></span>
    <div class="social"><span></span><span></span><span></span><span></span></div>
    <div class="legal">© 2016 wheelsforheroes.org. All Copyrights are Reserved.<br><a href="#">Terms of Use</a><a href="#">Privacy Policy</a><a href="#">Sitemap</a></div>
    <span class="code">C4</span>
  </div>
</footer>

</body>
</html>
```